Natural, organic, vegan-friendly nutritious food supplements

We need packaging design for a new nutritious food supplement to be launched. The products are organic, natural, with no additives, lactose-free, gluten-free, vegan-friendly, etc. The product is a powder that comes in 40g sachets (need sachet design) which are then put into a box (need box design).

More details in the included zip file. Please do not hesitate to contact us for more information if needed.

Target Market(s)

Everyone interested in healthy food.

Requirements
Must have
• Vibrant colours, must be easy to read and easy to recognise on a shelf.
Natural colours.

```html
<!DOCTYPE html>
<html lang="en">
<head>
<meta charset="utf-8">
<title>Coco Craving – Coconut &amp; Vanilla packaging</title>
<link rel="stylesheet" href="https://fonts.googleapis.com/css2?family=Oswald:wght@700&family=Josefin+Sans:wght@400;700&family=Baloo+2:wght@700&family=Open+Sans:wght@400;600;700&display=swap">
<style>
  :root{
    --brown:#6b3e2e;
    --brown-soft:#8a5238;
    --ink:#2a2a2a;
    --grey-text:#4a4f4f;
    --panel:#f4f5f4;
    --panel-edge:#e2e5e4;
    --green:#3aa541;
    --green-band:#9bd27a;
    --bg-top:#fbfbfb;
    --bg-bottom:#c2cbca;
  }
  *{box-sizing:border-box;margin:0;padding:0}
  html,body{width:1200px;height:1200px;overflow:hidden}
  body{background:linear-gradient(var(--bg-top),var(--bg-bottom));position:relative;font-family:"Open Sans",sans-serif;color:var(--ink)}
  .abs{position:absolute}
  .page-title{left:0;width:1200px;top:118px;text-align:center;white-space:nowrap;font-family:"Oswald",sans-serif;font-weight:700;font-size:74px;line-height:100px;letter-spacing:4px;color:var(--brown);transform:scaleY(1.3);transform-origin:50% 50%}
  .caption{font-family:"Open Sans",sans-serif;font-size:22px;color:var(--grey-text);text-align:center}

  /* box */
  .box-tab{left:87px;top:320px;width:474px;height:260px;background:#fafbfa;border:1px solid var(--panel-edge)}
  .hang-hole{left:135px;top:28px}
  .box-front{left:70px;top:578px;width:503px;height:340px;background:var(--panel);border:1px solid var(--panel-edge)}
  .brand{display:flex;flex-direction:column;align-items:center;justify-content:center;border:1.5px solid var(--ink);border-radius:50%;font-family:"Josefin Sans",sans-serif;font-weight:700;color:var(--ink)}
  .brand-lg{left:170px;top:90px;width:136px;height:136px;font-size:30px;letter-spacing:2px}
  .brand-sm{left:30px;top:16px;width:72px;height:72px;font-size:16px;letter-spacing:1px}
  .organic-badge{width:20px;height:14px;border:1.5px solid var(--green);border-radius:2px;background:#fff}
  .organic-badge::after{content:"";position:absolute;left:3px;top:2px;width:11px;height:7px;background:var(--green);border-radius:50%}
  .product-name{font-family:"Josefin Sans",sans-serif;font-weight:700;color:var(--brown);text-align:center;letter-spacing:3px}
  .box-name{left:180px;top:30px;width:290px;font-size:25px;line-height:31px}
  .slogan{left:27px;top:116px;width:215px;font-family:"Baloo 2",sans-serif;font-weight:700;font-size:21px;line-height:31px;color:var(--brown-soft);white-space:nowrap}
  .tagline{font-size:7.5px;line-height:11px;color:var(--ink)}
  .box-tagline{left:27px;top:218px;width:200px}
  .art{background:radial-gradient(ellipse at 50% 50%,#f1f1ea 0%,#6e5a44 38%,#4f7a3a 60%,rgba(120,160,80,0) 75%)}
  .box-art{left:240px;top:122px;width:255px;height:120px}
  .box-flavour{left:0;width:503px;top:266px;text-align:center;white-space:nowrap;font-family:"Baloo 2",sans-serif;font-weight:700;font-size:29px;letter-spacing:1.2px;color:var(--brown)}
  .net{font-weight:700;color:var(--ink);text-align:center}
  .box-net{left:0;width:503px;top:314px;font-size:12.5px;letter-spacing:.5px}

  /* pouches */
  .pouch{background:linear-gradient(90deg,#e9ebea,#fbfbfb 20%,#fbfbfb 80%,#e4e6e5);border:1px solid var(--panel-edge);overflow:hidden}
  .crimp{left:0;right:0;height:30px;background:repeating-linear-gradient(#f4f5f4 0 3px,#dfe2e1 3px 5px)}
  .crimp.top{top:0}.crimp.bottom{bottom:0}
  .pouch-back{left:820px;top:430px;width:322px;height:448px}
  .pouch-front{left:640px;top:555px;width:322px;height:446px}

  .front-brand{left:120px;top:62px;width:86px;height:86px;font-size:20px}
  .front-art{left:48px;top:165px;width:220px;height:118px}
  .front-name{left:0;width:322px;top:320px;font-family:"Open Sans",sans-serif;font-weight:400;font-size:17px;color:var(--ink);text-align:center;letter-spacing:.2px}
  .front-flavour{left:0;width:322px;top:342px;font-size:10.5px;color:var(--brown);text-align:center;letter-spacing:.8px;font-weight:600}
  .front-tagline{left:70px;width:182px;top:358px;text-align:center;font-size:6.5px;line-height:9px}
  .front-net{left:0;width:322px;top:387px;font-size:7px}

  .back-name{left:0;width:322px;top:74px;font-size:13px;letter-spacing:1px;font-weight:400}
  .prep{left:48px;top:106px;width:103px;font-size:5.5px;line-height:8px}
  .prep b{font-style:italic}
  .ingredients{left:110px;top:195px;width:42px;font-size:5.5px;line-height:9.5px;text-align:right}
  .nutri{left:156px;top:103px;width:130px;border-collapse:collapse;font-size:4.3px;line-height:5.6px;background:#fff}
  .nutri td,.nutri th{border:.5px solid #999;padding:0 2px;text-align:left;font-weight:400}
  .nutri th{font-weight:700}
  .nutri .band td{background:var(--green-band);font-weight:700}
  .back-badge{left:128px;top:258px}
  .splash{left:120px;top:290px;width:80px;height:90px;background:radial-gradient(ellipse,#f2dc87 0%,rgba(242,220,135,0) 70%)}
  .back-art{left:180px;top:285px;width:112px;height:72px}
  .back-meta{left:150px;width:142px;text-align:right;font-size:7.5px;line-height:14px;color:var(--ink)}
  .back-meta .flav{font-size:10px;color:var(--brown);letter-spacing:.8px;font-weight:600}
</style>
</head>
<body>

<h1 class="abs page-title">COCONUT &amp; VANILLA FLAVOUR</h1>

<!-- sachet box -->
<section class="abs box-tab" aria-label="Box hanging tab">
  <svg class="abs hang-hole" width="205" height="60" viewBox="0 0 205 60">
    <path d="M20 34 H85 Q90 34 92 24 Q95 14 102 14 Q110 14 113 24 Q115 34 120 34 H185 Q200 34 200 47 Q200 60 185 60 H20 Q5 60 5 47 Q5 34 20 34Z" fill="#dcdedd" stroke="#c9cccb"/>
  </svg>
  <div class="abs brand brand-lg">VERDA</div>
</section>

<section class="abs box-front" aria-label="Sachet box front">
  <div class="abs brand brand-sm">VERDA</div>
  <div class="abs organic-badge" style="left:466px;top:6px" role="img" aria-label="Certification badge"></div>
  <h2 class="abs product-name box-name">COCO<br>CRAVING</h2>
  <p class="abs slogan">Positive Side Effects<br>Of Living Are Entirely<br>Intentional !!</p>
  <p class="abs tagline box-tagline">More delicate flavour profile but with a hint of sourness. Easy to drink and nice in flavour.</p>
  <div class="abs art box-art" role="img" aria-label="Illustration of split coconut with vanilla flowers and green leaves"></div>
  <p class="abs box-flavour">COCONUT &amp; VANILLA FLAVOUR</p>
  <p class="abs net box-net">NET WEIGHT: 600g (15 x 40g)</p>
</section>
<p class="abs caption" style="left:70px;width:512px;top:940px">sachet box front side</p>

<!-- sachet back -->
<p class="abs caption" style="left:820px;width:322px;top:392px">sachet pouch back</p>
<section class="abs pouch pouch-back" aria-label="Sachet pouch back">
  <div class="abs crimp top"></div><div class="abs crimp bottom"></div>
  <h2 class="abs product-name back-name">COCO CRAVING</h2>
  <p class="abs prep"><b>Preparation:</b> shake the contents with 200ml of your preferred liquid and enjoy.</p>
  <p class="abs ingredients">Ingredients: coconut powder, organic chia, organic rice, maca, vanilla.</p>
  <table class="abs nutri">
    <tr><th colspan="3">Nutrition Facts: Coconut &amp; Vanilla</th></tr>
    <tr><td></td><td>Per 100g</td><td>Per 40g</td></tr>
    <tr><td>Energy kcal</td><td>380</td><td>152</td></tr>
    <tr><td>Fat g</td><td>12</td><td>4.8</td></tr>
    <tr><td>Saturates g</td><td>8.2</td><td>3.3</td></tr>
    <tr><td>Carbohydrate g</td><td>48</td><td>19</td></tr>
    <tr><td>Sugars g</td><td>9</td><td>3.6</td></tr>
    <tr><td>Fibre g</td><td>14</td><td>5.6</td></tr>
    <tr><td>Protein g</td><td>18</td><td>7.2</td></tr>
    <tr><td>Salt g</td><td>0.1</td><td>0.04</td></tr>
    <tr class="band"><td colspan="3">Vitamins</td></tr>
    <tr><td>Vitamin C mg</td><td>60</td><td>24</td></tr>
    <tr><td>Vitamin E mg</td><td>8</td><td>3.2</td></tr>
    <tr><td>Vitamin B6 mg</td><td>1.2</td><td>0.5</td></tr>
    <tr class="band"><td colspan="3">Minerals</td></tr>
    <tr><td>Calcium mg</td><td>300</td><td>120</td></tr>
    <tr><td>Iron mg</td><td>8</td><td>3.2</td></tr>
    <tr><td>Magnesium mg</td><td>200</td><td>80</td></tr>
    <tr><td>Zinc mg</td><td>6</td><td>2.4</td></tr>
  </table>
  <div class="abs organic-badge back-badge" role="img" aria-label="Certification badge"></div>
  <div class="abs splash" role="img" aria-label="Splash of creamy drink"></div>
  <div class="abs art back-art" role="img" aria-label="Illustration of coconut with vanilla flowers and leaves"></div>
  <div class="abs back-meta" style="top:352px">
    <div>Produced in Denmark</div>
    <div>New Nutritious Food Supplement</div>
    <div class="flav">COCONUT &amp; VANILLA</div>
  </div>
</section>

<!-- sachet front -->
<section class="abs pouch pouch-front" aria-label="Sachet pouch front">
  <div class="abs crimp top"></div><div class="abs crimp bottom"></div>
  <div class="abs brand front-brand">VERDA</div>
  <div class="abs art front-art" role="img" aria-label="Illustration of split coconut with vanilla flowers and green leaves"></div>
  <h2 class="abs front-name">COCO CRAVING</h2>
  <p class="abs front-flavour">COCONUT &amp; VANILLA FLAVOUR</p>
  <p class="abs tagline front-tagline">More delicate flavour profile but with a hint of sourness. Easy to drink and nice in flavour</p>
  <p class="abs net front-net">NET WEIGHT: 40G</p>
</section>
<p class="abs caption" style="left:640px;width:322px;top:1022px">sachet pouch front</p>

</body>
</html>
```